Business card, postcard, pocket folder

We are a real estate team and have had a new logo designed. From this, we need the following deliverables:- Business Cards (double-sided)- Just Listed / Just Sold Postcards (double-sided)- Pocket Folder. See logo attached.More work possible for the winning designer.
There are 5 members of the team, so head shots should be easily changed and possible for a group photo might be a good idea for the pocket folder but not 100% neccessary.
Target Market(s)
Real estate
Industry/Entity Type
Real Estate
Font styles to use
Serif
Sans Serif
Requirements
Must have
- Business cards and postcards must have a head shot on them.

```html
<!DOCTYPE html>
<html lang="en">
<head>
<meta charset="utf-8">
<title>Vantorel Group – Business Card</title>
<link rel="stylesheet" href="https://fonts.googleapis.com/css2?family=Roboto:wght@300;400;500;700&display=swap">
<style>
  :root {
    --brand-blue: #233a95;
    --brand-red: #d9001b;
    --text-grey: #555555;
    --portrait-grey: #8a8a8a;
    --card-white: #ffffff;
    --page-bg: #eeeeee;
  }
  * { margin: 0; padding: 0; box-sizing: border-box; }
  html, body {
    width: 1125px; height: 1200px; overflow: hidden;
    background: var(--page-bg);
    font-family: "Roboto", Arial, sans-serif;
  }
  .sheet { position: relative; width: 1125px; height: 1200px; }
  .card {
    position: absolute; left: 171px;
    width: 800px; height: 457px;
    transform: scale(1.032); transform-origin: top left;
    overflow: hidden;
  }
  .card--front { top: 106px; background: var(--card-white); }
  .card--back { top: 639px; background: var(--brand-blue); }

  .wordmark {
    position: absolute; font-weight: 500; letter-spacing: -0.5px; white-space: nowrap;
  }
  .card--front .wordmark {
    right: 53px; top: 142px; font-size: 44px; color: var(--brand-blue);
  }
  .holder { position: absolute; left: 50px; top: 204px; }
  .holder__name { font-size: 30px; font-weight: 700; color: var(--brand-blue); line-height: 1.1; }
  .holder__title { font-size: 19px; font-weight: 400; color: var(--brand-red); margin-top: 4px; }
  .divider {
    position: absolute; left: 50px; top: 276px; width: 697px; height: 2px; background: var(--brand-red);
  }
  .contacts { position: absolute; left: 50px; top: 292px; list-style: none; }
  .contacts li {
    display: flex; align-items: center; height: 25.5px;
    font-size: 19px; font-weight: 300; color: var(--text-grey);
  }
  .contacts svg { width: 18px; height: 18px; margin-right: 12px; fill: var(--brand-red); }
  .address {
    position: absolute; right: 53px; top: 292px; text-align: right;
    font-size: 19px; font-weight: 300; color: var(--text-grey); line-height: 25.5px; font-style: normal;
  }
  .bands { position: absolute; left: 0; top: 410px; }
  .front-url {
    position: absolute; right: 53px; top: 424px;
    font-size: 19px; font-weight: 300; color: var(--card-white);
  }

  .portrait {
    position: absolute; left: 384px; top: 40px; width: 416px; height: 417px;
    background: var(--portrait-grey); border-radius: 140px 140px 0 0;
  }
  .back-brand { position: absolute; left: 50px; top: 296px; width: 340px; text-align: center; }
  .card--back .wordmark { position: static; font-size: 46px; color: var(--card-white); }
  .back-url {
    margin-top: 22px; font-size: 18px; font-weight: 400; letter-spacing: 5px; color: var(--card-white);
  }
</style>
</head>
<body>
<main class="sheet">
  <section class="card card--front" aria-label="Business card front">
    <div class="wordmark">Vantorel Group</div>

    <div class="holder">
      <div class="holder__name">Daniel Reyes</div>
      <div class="holder__title">CEO/Founder</div>
    </div>
    <div class="divider"></div>

    <ul class="contacts">
      <li><svg viewBox="0 0 24 24" aria-hidden="true"><path d="M6.6 10.8a15.1 15.1 0 0 0 6.6 6.6l2.2-2.2a1 1 0 0 1 1-.25 11.4 11.4 0 0 0 3.6.57 1 1 0 0 1 1 1V20a1 1 0 0 1-1 1A17 17 0 0 1 3 4a1 1 0 0 1 1-1h3.5a1 1 0 0 1 1 1c0 1.25.2 2.45.57 3.57a1 1 0 0 1-.25 1z"/></svg>555 201 4817</li>
      <li><svg viewBox="0 0 24 24" aria-hidden="true"><path d="M7 1h10a2 2 0 0 1 2 2v18a2 2 0 0 1-2 2H7a2 2 0 0 1-2-2V3a2 2 0 0 1 2-2zm0 3v15h10V4zm5 16.2a.9.9 0 1 0 0 1.8.9.9 0 0 0 0-1.8z"/></svg>555 734 2290</li>
      <li><svg viewBox="0 0 24 24" aria-hidden="true"><path d="M6 2h10l2 2v5H6zM3 10h18a2 2 0 0 1 2 2v7H1v-7a2 2 0 0 1 2-2zm3 6v6h12v-6z"/></svg>555 618 3052</li>
      <li><svg viewBox="0 0 24 24" aria-hidden="true"><path d="M2 5h20v14H2zm2 2v.5l8 5 8-5V7l-8 5z"/></svg>daniel@vantorel.com</li>
    </ul>

    <address class="address">3218 Juniper Lane<br>Fairbanks, Alaska 99701</address>

    <svg class="bands" width="800" height="47" viewBox="0 0 800 47" aria-hidden="true">
      <polygon points="0,17 487,17 479,25 0,25" fill="var(--brand-blue)"/>
      <polygon points="0,30 800,30 800,47 0,47" fill="var(--brand-red)"/>
      <polygon points="511,4 800,4 800,47 470,47" fill="var(--brand-red)"/>
      <polygon points="487,17 501,4 511,4 484,28 0,28 0,25 479,25" fill="var(--card-white)"/>
    </svg>
    <div class="front-url">www.vantorel.com</div>
  </section>

  <section class="card card--back" aria-label="Business card back">
    <div class="portrait" role="img" aria-label="Head shot of the agent in suit and tie"></div>
    <div class="back-brand">
      <div class="wordmark">Vantorel Group</div>
      <div class="back-url">www.vantorel.com</div>
    </div>
  </section>
</main>
</body>
</html>
```